Movie poster for short film: TINFOIL

We need a creative, artistic, stylized poster design for our short film TINFOIL. We would like to see designs with graphics and bold colors more than photographs. The photographs we are posting are more for reference- you do not have to use them in the poster! We are looking for something clean and simple. The film is a drama so please don't make it funny. The mood of the film is thoughtful and introspective. Name of film should be in all caps. Things to include in the poster:
Name of film: TINFOIL
Velvet Harbor Pictures
Starring Marisa Calloway

Here is a brief plot synopsis: TINFOIL follows one night in the life of a rebellious young woman who breaks into a diner after hours with a can of spray paint. Her intentions change after she ends up discovering what's left of a love story.

The movie is somewhat experimental, set to music for part of it with no dialog. The whole movie takes place in an old fashioned diner.

Target Market(s)

Film festival attendees between the ages of 20-50

Industry/Entity Type

Movie

Font styles to use
Sans Serif

Requirements
Must have
• See project description above- also the film is somewhat dark in nature so please don't make it too 'happy' looking.

```html
<!DOCTYPE html>
<html lang="en">
<head>
<meta charset="utf-8">
<title>TINFOIL — Poster</title>
<link href="https://fonts.googleapis.com/css2?family=Montserrat:wght@700&family=Oswald:wght@400;600&display=swap" rel="stylesheet">
<style>
  :root {
    --bg-center: #1d3252;
    --bg-edge: #0a1322;
    --ink: #ffffff;
    --candy-red: #d8232a;
    --candy-pink: #ec7fa3;
    --candy-blue: #2a9fd0;
    --candy-yellow: #e6e53a;
    --candy-orange: #f0962a;
    --candy-green: #34b84a;
    --candy-white: #ecebe6;
  }
  html, body {
    margin: 0;
    padding: 0;
    width: 800px;
    height: 1200px;
    overflow: hidden;
    background: var(--bg-edge);
  }
  .poster {
    position: relative;
    width: 800px;
    height: 1200px;
    overflow: hidden;
    background: radial-gradient(ellipse 70% 55% at 50% 55%, var(--bg-center) 0%, #142540 55%, var(--bg-edge) 100%);
    color: var(--ink);
    text-align: center;
  }
  .studio {
    position: absolute;
    top: 62px;
    left: 0;
    right: 0;
    margin: 0;
    font-family: "Oswald", sans-serif;
    font-size: 25px;
    font-weight: 400;
    letter-spacing: 0.5px;
    text-transform: uppercase;
  }
  .studio strong { font-weight: 600; }
  .title {
    position: absolute;
    top: 118px;
    left: 0;
    right: 0;
    margin: 0;
    font-family: "Montserrat", sans-serif;
    font-weight: 700;
    font-size: 96px;
    line-height: 1;
    letter-spacing: 3px;
    text-transform: uppercase;
  }
  .billing {
    position: absolute;
    top: 238px;
    left: 0;
    right: 0;
    margin: 0;
    font-family: "Oswald", sans-serif;
    font-size: 29px;
    font-weight: 400;
    letter-spacing: 0.5px;
    text-transform: uppercase;
  }
  .billing strong { font-weight: 600; }
  .figure-art {
    position: absolute;
    left: 140px;
    top: 328px;
    width: 540px;
    height: 872px;
    border-radius: 240px 240px 0 0;
    background:
      radial-gradient(circle at 30% 20%, var(--candy-yellow) 0%, transparent 30%),
      radial-gradient(circle at 70% 35%, var(--candy-blue) 0%, transparent 35%),
      radial-gradient(circle at 35% 60%, var(--candy-pink) 0%, transparent 35%),
      radial-gradient(circle at 65% 80%, var(--candy-orange) 0%, transparent 35%),
      radial-gradient(circle at 25% 90%, var(--candy-green) 0%, transparent 30%),
      radial-gradient(circle at 55% 10%, var(--candy-white) 0%, transparent 25%),
      var(--candy-red);
  }
</style>
</head>
<body>
  <main class="poster">
    <p class="studio"><strong>Velvet Harbor</strong> Pictures</p>
    <h1 class="title">TINFOIL</h1>
    <p class="billing">Starring <strong>Marisa Calloway</strong></p>
    <div class="figure-art" role="img" aria-label="Side-profile silhouette of a young woman filled with many brightly coloured round candies"></div>
  </main>
</body>
</html>
```